Brambury Logistics

Create a modern, simple, Elegant business card design for my business.

Services: Tamo Trucks, Transport, Contract Logistics,

Industry/Entity Type

Business

Contact Information for Business Card

Include all details same as old card plus new website address: www.bramburylogistics.com.au

Requirements
Must have
• Similar colors to Logo.

```html
<!DOCTYPE html>
<html lang="en">
<head>
<meta charset="utf-8">
<title>Brambury Logistics – Business Card</title>
<link href="https://fonts.googleapis.com/css2?family=Open+Sans:wght@400;600;700&display=swap" rel="stylesheet">
<style>
  :root {
    --stage: #000000;
    --card-navy: #21405c;
    --card-white: #ffffff;
    --text-light: #ffffff;
    --brand-grey: #6f7378;
    --brand-blue: #1f6fb5;
  }
  * { margin: 0; padding: 0; box-sizing: border-box; }
  html, body {
    width: 1200px;
    height: 900px;
    overflow: hidden;
    background: var(--stage);
    font-family: "Open Sans", Arial, sans-serif;
  }
  .canvas {
    position: relative;
    width: 1200px;
    height: 900px;
  }
  .card {
    position: absolute;
    top: 271px;
    width: 457px;
    height: 281px;
    border-radius: 13px;
  }
  .card--front {
    left: 137px;
    background: var(--card-navy);
    color: var(--text-light);
    text-align: center;
  }
  .card--back {
    left: 626px;
    background: var(--card-white);
  }
  .wordmark {
    position: absolute;
    left: 0;
    right: 0;
    font-weight: 700;
    letter-spacing: 0.5px;
    white-space: nowrap;
  }
  .card--front .wordmark {
    top: 36px;
    font-size: 27px;
    color: var(--text-light);
  }
  .card--back .wordmark {
    top: 112px;
    font-size: 34px;
    color: var(--brand-grey);
    text-align: center;
  }
  .contact {
    position: absolute;
    left: 0;
    right: 0;
    top: 121px;
  }
  .contact__name {
    font-size: 17px;
    font-weight: 700;
    line-height: 20px;
  }
  .contact__role {
    font-size: 16px;
    line-height: 20px;
  }
  .contact__lines {
    margin-top: 14px;
    font-size: 14px;
    line-height: 17.5px;
  }
  .contact__address {
    position: absolute;
    left: 0;
    right: 0;
    top: 248px;
    font-size: 12.5px;
  }
</style>
</head>
<body>
  <main class="canvas">
    <section class="card card--front">
      <div class="wordmark">Brambury Logistics</div>
      <div class="contact">
        <div class="contact__name">Alan Moreton</div>
        <div class="contact__role">Director</div>
        <div class="contact__lines">
          <div class="contact__phone">312-408-05192</div>
          <div class="contact__email">info@brambury.com</div>
          <div class="contact__web">www.bramburylogistics.com.au</div>
        </div>
      </div>
      <div class="contact__address">248 W. Harlow Suite 910. Chicago, Illinois 60601</div>
    </section>

    <section class="card card--back">
      <div class="wordmark">Brambury Logistics</div>
    </section>
  </main>
</body>
</html>
```